I am medical doctor in surgery specialized in Urology and anti-aging. I need Web and Instagram design for a head cream , face cream and body lotion. I did a 2% GHK-Cu solution (head-face-body) with an professional pharmacist specialized in manufacturing creams. . GHK-Cu is a tri-peptide with solid scientific background to rejuvenate the skin (will stimulate collagen production) and can promote hair regrowth. Statistically 70% of peptides bought are fake on the market, I can personally guarantee about purity (my peptides are certified pure above 99% checked in an independent laboratory in London -UK.
I want to use the name 'Lunavel'. I secured already the domain names. I had an design for another project I could re-use for this project. The ribbon should include more blue. The font of Lunavel can be changed. I got a logo which is ok for me. Web design best coded with Wordpress.

Target Market(s)

Anti aging, skin care, hair regrowth, skin collagen

Industry/Entity Type

the cream can also be used after surgery for faster and better wound healing

Number of Pages Required

5+ page

Font styles to use
Sans Serif

Colors
0054AA
0677BA
7BADD7
CADEEF
E8F1F8

Requirements
Must have
• target population 30-70 years
Nice to have
• scientific proof, pictures before-after
Should not have
• GHK-Cu has solid scientific animal studies of anti-cancer properties. It is 100% safe for dermal human use.

```html
<!DOCTYPE html>
<html lang="en">
<head>
<meta charset="utf-8">
<title>Lunavel — Pure GHK-Cu</title>
<link href="https://fonts.googleapis.com/css2?family=Outfit:wght@300;400;500;600;700&family=Cormorant+Garamond:ital,wght@1,500&display=swap" rel="stylesheet">
<style>
:root{
  --blue:#0a8be6;
  --blue-deep:#0677ba;
  --navy:#0b2a6b;
  --ink:#0d2c73;
  --text:#2b2f3a;
  --muted:#4a5262;
  --pale:#e8f1f8;
  --card:#f5f9fd;
  --line:#cadeef;
  --white:#fff;
}
*{box-sizing:border-box;margin:0;padding:0}
html,body{width:1200px;height:3868px;overflow:hidden}
body{font-family:"Outfit",sans-serif;color:var(--text);background:var(--white);position:relative}
.abs{position:absolute}
a{color:inherit;text-decoration:none}

/* header */
.site-header{left:0;top:0;width:1200px;height:85px;background:var(--white)}
.brand{display:flex;align-items:center;gap:8px;font-weight:600;font-size:24px;color:var(--blue-deep)}
.brand-dot{width:26px;height:26px;border-radius:50%;background:var(--blue)}
.site-header .brand{position:absolute;left:140px;top:26px}
.main-nav{position:absolute;top:34px;left:0;width:1200px;font-size:11.5px;font-weight:400;color:#1a1f2b;letter-spacing:.3px}
.main-nav a{position:absolute;transform:translateX(-50%);white-space:nowrap}
.header-icons{position:absolute;left:946px;top:30px;display:flex;gap:14px}
.header-icons svg{width:18px;height:18px;stroke:#1a1f2b;fill:none;stroke-width:1.8}
.cart{position:relative}
.cart-badge{position:absolute;right:-4px;bottom:-4px;width:10px;height:10px;border-radius:50%;background:var(--blue);color:#fff;font-size:7px;text-align:center;line-height:10px}

/* hero */
.hero{left:0;top:85px;width:1200px;height:531px;overflow:hidden}
.hero-visual{position:absolute;inset:0;background:
  radial-gradient(ellipse 340px 260px at 900px 260px,#f4f8fc 0%,rgba(244,248,252,0) 100%),
  radial-gradient(ellipse 200px 200px at 1010px 230px,rgba(150,215,220,.55) 0%,rgba(150,215,220,0) 100%),
  linear-gradient(100deg,#f1f6fb 0%,#dde9f4 40%,#b3cde4 75%,#9fbfdb 100%)}
.hero-copy{position:absolute;left:141px;top:88px}
.eyebrow{border-left:2px solid var(--ink);padding-left:10px;font-size:15px;color:#1a1f2b;height:26px;line-height:26px}
.hero h1{margin-top:20px;font-size:51px;line-height:64px;font-weight:700;color:#10131c}
.hero h1 em{font-family:"Cormorant Garamond",serif;font-style:italic;font-weight:500;font-size:56px}
.hero p{margin-top:20px;font-size:13.5px;line-height:23px;color:#1a1f2b}
.btn-shop{margin-top:22px;display:inline-flex;align-items:center;gap:22px;background:var(--blue-deep);color:#fff;height:40px;padding:0 6px 0 24px;border-radius:20px;font-size:12px;font-weight:500}
.btn-shop span.arrow{width:30px;height:30px;border-radius:50%;background:#fff;display:flex;align-items:center;justify-content:center}

/* trust band */
.trust{left:0;top:616px;width:1200px;height:108px;background:var(--blue)}
.trust-strip{left:0;top:724px;width:1200px;height:12px;background:var(--navy)}
.trust-item{position:absolute;top:27px;display:flex;align-items:center;gap:14px;color:#fff;font-size:14px;line-height:17px}
.trust-icon{width:55px;height:55px;border-radius:50%;background:#fff;display:flex;align-items:center;justify-content:center}
.trust-icon svg{width:30px;height:30px;stroke:var(--blue);fill:none;stroke-width:1.8}

/* section headings */
.kicker{width:1200px;left:0;text-align:center;font-size:11px;color:var(--blue)}
.section-title{width:1200px;left:0;text-align:center;font-size:32px;font-weight:600;color:var(--ink)}
.section-sub{width:1200px;left:0;text-align:center;font-size:13.5px;color:var(--ink)}

/* solution cards */
.solution{top:865px;width:317px;height:252px;background:#fff;border-radius:8px;box-shadow:0 2px 10px rgba(10,40,100,.08);border-bottom:5px solid var(--blue);overflow:hidden}
.solution .photo{position:absolute;left:0;top:0;width:158px;height:247px}
.solution .info{position:absolute;left:170px;top:16px;width:136px}
.solution h3{font-size:14px;font-weight:600;color:var(--ink)}
.solution .tag{font-size:10.5px;color:var(--blue);text-decoration:underline;margin-top:2px}
.solution p{font-size:11px;line-height:20px;color:#2b2f3a;margin-top:8px}
.solution .more{position:absolute;left:170px;top:204px;font-size:11px;color:var(--ink)}

/* product cards */
.product{width:234px;height:311px;background:var(--card);border:1px solid #e3edf7;border-radius:6px;text-align:center}
.product .wish{position:absolute;right:12px;top:14px;width:17px;height:17px;stroke:var(--blue);fill:none;stroke-width:1.8}
.product .thumb{position:absolute;left:64px;top:21px;width:106px;height:106px;border-radius:50%;background:radial-gradient(circle at 50% 40%,#ffffff 0%,#dce8f4 70%,#cadeef 100%);overflow:hidden}
.product .thumb::after{content:"";position:absolute;left:18px;top:30px;width:70px;height:60px;border-radius:10px;background:var(--tone)}
.serum{--tone:linear-gradient(180deg,#d9b77a 0%,#b88a4a 60%,#e9e4dc 100%)}
.renewal{--tone:linear-gradient(180deg,#f4f1ec 0%,#d8cfc2 60%,#c9a667 100%)}
.scalp{--tone:linear-gradient(180deg,#a9a1d6 0%,#6f62b3 70%,#4c3f94 100%)}
.booster{--tone:linear-gradient(180deg,#ebe1d4 0%,#d6c5ae 60%,#b9bcc2 100%)}
.product h4{position:absolute;top:138px;width:100%;font-size:17px;font-weight:600;color:var(--ink)}
.product .price{position:absolute;top:164px;width:100%;font-size:18px;font-weight:600;color:var(--blue)}
.product .desc{position:absolute;top:190px;left:36px;width:162px;font-size:11px;line-height:21px;color:var(--muted)}
.btn-cart{position:absolute;left:66px;top:252px;width:102px;height:32px;line-height:32px;background:var(--blue);color:#fff;font-size:11px;border-radius:3px;text-align:center}

/* feature */
.feature-photo{left:0;top:1708px;width:600px;height:630px;background:
  radial-gradient(ellipse 180px 260px at 300px 330px,#f7f5f2 0%,rgba(247,245,242,0) 100%),
  linear-gradient(160deg,#ebe7e2 0%,#dcd4ca 50%,#c9c0b4 100%)}
.play{position:absolute;left:270px;top:285px;width:60px;height:60px;border-radius:50%;background:rgba(255,255,255,.55);display:flex;align-items:center;justify-content:center}
.feature-card{left:435px;top:1792px;width:658px;height:456px;background:#fff;border-left:12px solid var(--blue);box-shadow:0 4px 24px rgba(10,40,100,.08)}
.feature-card h3{position:absolute;left:43px;top:80px;font-size:17px;font-weight:600;color:var(--ink)}
.feature-card .lead{position:absolute;left:46px;top:114px;font-size:11px;color:#2b2f3a}
.feature-card .body{position:absolute;left:46px;top:144px;width:522px;font-size:11px;line-height:20.5px;color:#2b2f3a}
.feature-card .big-price{position:absolute;left:43px;top:232px;font-size:42px;font-weight:400;color:#1a1f2b}
.feature-card .btn-cart{left:43px;top:298px;width:102px}
.ornament{border-radius:6px;background:linear-gradient(135deg,rgba(31,99,216,.18) 0%,rgba(22,162,232,.18) 45%,rgba(247,178,28,.18) 100%)}

/* results */
.results-bg-left{left:0;top:2666px;width:345px;height:252px;background:var(--blue)}
.results-bg-right{left:345px;top:2666px;width:855px;height:252px;background:var(--navy)}
.result{top:2490px;width:473px;height:320px;background:#fff;border-radius:6px;overflow:hidden;box-shadow:0 3px 14px rgba(10,40,100,.12)}
.result .photo{position:absolute;left:0;top:0;width:100%;height:248px}
.result .cap{position:absolute;top:273px;width:100%;text-align:center;font-size:14.5px;font-weight:600;color:var(--ink)}

/* cta + footer */
.cta{left:0;top:3471px;width:1200px;height:180px;background:var(--blue);text-align:center}
.cta h2{margin-top:46px;font-size:33px;font-weight:600;color:#fff}
.cta a{display:inline-block;margin-top:20px;width:144px;height:32px;line-height:32px;background:#fff;color:var(--ink);font-size:11px;border-radius:3px}
.site-footer{left:0;top:3651px;width:1200px;height:217px;background:var(--navy)}
.site-footer .brand{position:absolute;left:530px;top:52px;color:#fff;font-size:28px}
.contact{position:absolute;top:64px;display:flex;align-items:center;gap:8px;color:#fff;font-size:11px}
.contact svg{width:16px;height:16px;stroke:#fff;fill:none;stroke-width:1.6}
.foot-nav{position:absolute;top:146px;left:0;width:1200px;font-size:11px;color:#fff}
.foot-nav a{position:absolute;transform:translateX(-50%);white-space:nowrap}
.foot-nav i{position:absolute;top:0;width:1px;height:14px;background:rgba(255,255,255,.35)}
.copyright{position:absolute;top:180px;width:100%;text-align:center;font-size:10.5px;color:#fff}
</style>
</head>
<body>

<header class="site-header abs">
  <a class="brand" href="#"><span class="brand-dot"></span>Lunavel</a>
  <nav class="main-nav">
    <a style="left:383px">HOME</a><a style="left:448px">SHOP</a><a style="left:526px">PRODUCTS</a><a style="left:611px">SCIENCE</a><a style="left:687px">PURITY</a><a style="left:766px">ABOUT US</a><a style="left:860px">CONTACT US</a>
  </nav>
  <div class="header-icons">
    <svg viewBox="0 0 24 24"><circle cx="10" cy="10" r="6.5"/><path d="M15 15l6 6"/></svg>
    <svg viewBox="0 0 24 24"><circle cx="12" cy="8" r="4.5"/><path d="M3.5 21c1-4.5 4.5-6.5 8.5-6.5s7.5 2 8.5 6.5z"/></svg>
    <svg viewBox="0 0 24 24"><path d="M12 20s-8-5-8-11a4.5 4.5 0 0 1 8-2.7A4.5 4.5 0 0 1 20 9c0 6-8 11-8 11z"/></svg>
    <span class="cart"><svg viewBox="0 0 24 24"><path d="M5 7h14l-1 14H6z"/><path d="M9 7a3 3 0 0 1 6 0"/></svg><span class="cart-badge">0</span></span>
  </div>
</header>

<section class="hero abs">
  <div class="hero-visual" role="img" aria-label="Cream jar, pump bottle and tubes on a pale blue surface with a cream swirl"></div>
  <div class="hero-copy">
    <div class="eyebrow">Enhance Your Natural Beauty</div>
    <h1>Rejuvenate <em>Your</em><br><em>Skin &amp; Hair</em> With<br>Pure GHK-Cu</h1>
    <p>Clinically-inspired 2% GHK-Cu creams. Certified purity.<br>Visible collagen boost &amp; hair regrowth.</p>
    <a class="btn-shop" href="#">SHOP NOW <span class="arrow"><svg width="14" height="14" viewBox="0 0 24 24" fill="none" stroke="#0677ba" stroke-width="2.4"><path d="M7 17L17 7M9 7h8v8"/></svg></span></a>
  </div>
</section>

<section class="trust abs">
  <div class="trust-item" style="left:105px"><span class="trust-icon"><svg viewBox="0 0 24 24"><rect x="4" y="3" width="16" height="18" rx="2"/><path d="M8 8h8M8 12h5"/><circle cx="15" cy="16" r="2.5"/></svg></span>99% Certified<br>Pure Peptides</div>
  <div class="trust-item" style="left:311px"><span class="trust-icon"><svg viewBox="0 0 24 24"><circle cx="12" cy="7" r="4"/><path d="M4 21c1-5 4-7 8-7s7 2 8 7z"/><path d="M12 14v4"/></svg></span>Medical Doctor<br>Developed</div>
  <div class="trust-item" style="left:511px"><span class="trust-icon"><svg viewBox="0 0 24 24"><rect x="5" y="4" width="14" height="17" rx="2"/><path d="M9 4v-1h6v1M8 10l1.5 1.5L12 9M8 15l1.5 1.5L12 14M14 10h2M14 15h2"/></svg></span>Independent<br>UK Laboratory<br>Tested</div>
  <div class="trust-item" style="left:709px"><span class="trust-icon"><svg viewBox="0 0 24 24"><path d="M9 3h6M10 3v6l-5 10a1.5 1.5 0 0 0 1.3 2h11.4a1.5 1.5 0 0 0 1.3-2L14 9V3"/><path d="M7 15h10"/></svg></span>Pharmaceutical<br>Grade Formulat</div>
  <div class="trust-item" style="left:907px"><span class="trust-icon"><svg viewBox="0 0 24 24"><circle cx="8" cy="7" r="3"/><circle cx="16" cy="7" r="3"/><path d="M2 20c.5-4 3-6 6-6s5.5 2 6 6M10 20c.5-4 3-6 6-6s5.5 2 6 6"/></svg></span>Suitable for<br>Men &amp; Women</div>
</section>
<div class="trust-strip abs"></div>

<div class="kicker abs" style="top:780px">OUR PRODUCTS</div>
<h2 class="section-title abs" style="top:795px">Three Solutions. One Scientific Formula.</h2>

<article class="solution abs" style="left:105px">
  <div class="photo" role="img" aria-label="Woman in hair towel holding a head cream jar" style="background:linear-gradient(180deg,#f3efeb 0%,#e2d6cc 55%,#6f74b8 100%)"></div>
  <div class="info"><h3>Head Cream</h3><div class="tag">Hair Regrowth Support</div><p>Supports healthier hair follicles while improving scalp condition with advanced peptide technology.</p></div>
  <a class="more" href="#">Explore Head Cream →</a>
</article>
<article class="solution abs" style="left:441px">
  <div class="photo" role="img" aria-label="Woman applying face cream with a cream jar in front" style="background:linear-gradient(180deg,#efe8e1 0%,#d9c1a9 55%,#c9b08c 100%)"></div>
  <div class="info"><h3>Face Cream</h3><div class="tag">Anti-Aging Face Therapy</div><p>Helps improve skin firmness, elasticity and the appearance of wrinkles through collagen stimulation.</p></div>
  <a class="more" href="#">Explore Face Cream →</a>
</article>
<article class="solution abs" style="left:777px">
  <div class="photo" role="img" aria-label="Woman in towel applying body lotion to her shoulder" style="background:linear-gradient(180deg,#eef0f3 0%,#dccfc4 55%,#8a86bd 100%)"></div>
  <div class="info"><h3>Body Lotion</h3><div class="tag">Full Body Rejuvenation</div><p>Hydrates, nourishes and promotes smoother healthier skin throughout the body.</p></div>
  <a class="more" href="#">Explore Body Lotion →</a>
</article>

<div class="kicker abs" style="top:1199px">Shop</div>
<h2 class="section-title abs" style="top:1214px">Shop The Collection</h2>
<p class="section-sub abs" style="top:1262px">Premium GHK-Cu formulations for skin, scalp &amp; overall rejuvenation</p>

<article class="product abs" style="left:105px;top:1308px"><svg class="wish" viewBox="0 0 24 24"><path d="M12 20s-8-5-8-11a4.5 4.5 0 0 1 8-2.7A4.5 4.5 0 0 1 20 9c0 6-8 11-8 11z"/></svg><div class="thumb serum" role="img" aria-label="Three serum dropper bottles"></div><h4>GHK-Cu Serum</h4><div class="price">$68</div><p class="desc">Advanced transdermal serum · 30 ml · collagen booster</p><a class="btn-cart" href="#">Add To Cart</a></article>
<article class="product abs" style="left:359px;top:1308px"><svg class="wish" viewBox="0 0 24 24"><path d="M12 20s-8-5-8-11a4.5 4.5 0 0 1 8-2.7A4.5 4.5 0 0 1 20 9c0 6-8 11-8 11z"/></svg><div class="thumb renewal" role="img" aria-label="Open cream jar with gold lid"></div><h4>Renewal Cream</h4><div class="price">$82</div><p class="desc">Day &amp; night cream with GHK-Cu + hyaluronic acid</p><a class="btn-cart" href="#">Add To Cart</a></article>
<article class="product abs" style="left:605px;top:1308px"><svg class="wish" viewBox="0 0 24 24"><path d="M12 20s-8-5-8-11a4.5 4.5 0 0 1 8-2.7A4.5 4.5 0 0 1 20 9c0 6-8 11-8 11z"/></svg><div class="thumb scalp" role="img" aria-label="Violet scalp spray bottle"></div><h4>Scalp Elixir</h4><div class="price">$54</div><p class="desc">Targeted peptide spray · reactivates follicles</p><a class="btn-cart" href="#">Add To Cart</a></article>
<article class="product abs" style="left:859px;top:1308px"><svg class="wish" viewBox="0 0 24 24"><path d="M12 20s-8-5-8-11a4.5 4.5 0 0 1 8-2.7A4.5 4.5 0 0 1 20 9c0 6-8 11-8 11z"/></svg><div class="thumb booster" role="img" aria-label="Open beige cream jar with silver lid"></div><h4>Pro Booster</h4><div class="price">$44</div><p class="desc">Concentrated GHK-Cu · 5 ml · for professional use</p><a class="btn-cart" href="#">Add To Cart</a></article>

<div class="feature-photo abs" role="img" aria-label="Smiling woman in white bathrobe holding a cream jar">
  <span class="play"><svg width="20" height="22" viewBox="0 0 20 22"><path d="M3 2l15 9-15 9z" fill="#8a8a8a"/></svg></span>
</div>
<div class="feature-card abs">
  <h3>GHK-Cu complex</h3>
  <p class="lead">Stimulates collagen, elastin, and glycosaminoglycan synthesis.</p>
  <p class="body">Lorem ipsum dolor sit amet, consectetuer adipiscing elit, sed diam nonummy nibh euismod tincidunt ut laoreet dolore magna aliquam erat volutpat. Ut wisi enim ad minim veniam, quis nostrud exerci tation ullamcorper suscipit lobortis nisl ut aliquip ex ea commodo consequat. Duis autem vel eum iriure dolor in hendrerit in vulputate velit esse molestie consequat.</p>
  <div class="big-price">$68</div>
  <a class="btn-cart" href="#">Add To Cart</a>
</div>
<div class="ornament abs" role="img" aria-label="Decorative ribbon area" style="left:885px;top:2065px;width:208px;height:205px"></div>

<div class="kicker abs" style="top:2407px">Results</div>
<h2 class="section-title abs" style="top:2423px">Real Results</h2>
<div class="results-bg-left abs"></div>
<div class="results-bg-right abs"></div>
<div class="ornament abs" role="img" aria-label="Decorative ribbon area" style="left:0;top:2735px;width:210px;height:200px"></div>
<div class="ornament abs" role="img" aria-label="Decorative ribbon area" style="left:985px;top:2470px;width:215px;height:200px"></div>
<article class="result abs" style="left:105px">
  <div class="photo" role="img" aria-label="Woman in bathrobe applying face cream at a vanity" style="background:linear-gradient(100deg,#d9cfc2 0%,#f3efea 45%,#e6ddd3 100%)"></div>
  <div class="cap">Skin Firming &amp; Wrinkle Reduction (Face Cream)</div>
</article>
<article class="result abs" style="left:622px">
  <div class="photo" role="img" aria-label="Woman combing wet hair with a green comb" style="background:linear-gradient(100deg,#eeebe8 0%,#d9cdc2 55%,#c7b5a4 100%)"></div>
  <div class="cap">Visible Hair Regrowth (Head Cream) <span style="color:var(--blue)">⟶</span></div>
</article>

<div class="kicker abs" style="top:2980px">Shop</div>
<h2 class="section-title abs" style="top:2995px">Our Bestsellers</h2>
<p class="section-sub abs" style="top:3041px">Duis autem vel eum iriure dolor in hendrerit in vulputate velit esse.</p>

<article class="product abs" style="left:105px;top:3090px"><svg class="wish" viewBox="0 0 24 24"><path d="M12 20s-8-5-8-11a4.5 4.5 0 0 1 8-2.7A4.5 4.5 0 0 1 20 9c0 6-8 11-8 11z"/></svg><div class="thumb serum" role="img" aria-label="Three serum dropper bottles"></div><h4>GHK-Cu Serum</h4><div class="price">$68</div><p class="desc">Advanced transdermal serum · 30 ml · collagen booster</p><a class="btn-cart" href="#">Add To Cart</a></article>
<article class="product abs" style="left:359px;top:3090px"><svg class="wish" viewBox="0 0 24 24"><path d="M12 20s-8-5-8-11a4.5 4.5 0 0 1 8-2.7A4.5 4.5 0 0 1 20 9c0 6-8 11-8 11z"/></svg><div class="thumb renewal" role="img" aria-label="Open cream jar with gold lid"></div><h4>Renewal Cream</h4><div class="price">$82</div><p class="desc">Day &amp; night cream with GHK-Cu + hyaluronic acid</p><a class="btn-cart" href="#">Add To Cart</a></article>
<article class="product abs" style="left:605px;top:3090px"><svg class="wish" viewBox="0 0 24 24"><path d="M12 20s-8-5-8-11a4.5 4.5 0 0 1 8-2.7A4.5 4.5 0 0 1 20 9c0 6-8 11-8 11z"/></svg><div class="thumb scalp" role="img" aria-label="Violet scalp spray bottle"></div><h4>Scalp Elixir</h4><div class="price">$54</div><p class="desc">Targeted peptide spray · reactivates follicles</p><a class="btn-cart" href="#">Add To Cart</a></article>
<article class="product abs" style="left:859px;top:3090px"><svg class="wish" viewBox="0 0 24 24"><path d="M12 20s-8-5-8-11a4.5 4.5 0 0 1 8-2.7A4.5 4.5 0 0 1 20 9c0 6-8 11-8 11z"/></svg><div class="thumb booster" role="img" aria-label="Open beige cream jar with silver lid"></div><h4>Pro Booster</h4><div class="price">$44</div><p class="desc">Concentrated GHK-Cu · 5 ml · for professional use</p><a class="btn-cart" href="#">Add To Cart</a></article>

<section class="cta abs">
  <h2>Experience the Power of Pure GHK-Cu</h2>
  <a href="#">Shop Our Collection</a>
</section>

<footer class="site-footer abs">
  <div class="contact" style="left:355px"><svg viewBox="0 0 24 24"><rect x="3" y="5" width="18" height="14" rx="1.5"/><path d="M3 6l9 7 9-7"/></svg>info@lunavel.com</div>
  <a class="brand" href="#"><span class="brand-dot"></span>Lunavel</a>
  <div class="contact" style="left:722px"><svg viewBox="0 0 24 24"><path d="M5 3h4l2 5-2.5 1.5a11 11 0 0 0 6 6L16 13l5 2v4a2 2 0 0 1-2 2A16 16 0 0 1 3 5a2 2 0 0 1 2-2z"/></svg>+44 20 7946 0321</div>
  <nav class="foot-nav">
    <a style="left:210px">Home</a><i style="left:256px"></i>
    <a style="left:302px">Science</a><i style="left:350px"></i>
    <a style="left:401px">Products</a><i style="left:455px"></i>
    <a style="left:524px">Clinical Evidence</a><i style="left:592px"></i>
    <a style="left:661px">Before &amp; After</a><i style="left:727px"></i>
    <a style="left:792px">About Doctor</a><i style="left:853px"></i>
    <a style="left:895px">FAQ</a><i style="left:937px"></i>
    <a style="left:984px">Contact</a>
  </nav>
  <div class="copyright">© 2026 Lunavel. All Rights Reserved.</div>
</footer>

</body>
</html>
```